Four in One (Flexible infographic for Content Management Industry)

See attachment.
A graphic depicting 4 products, where each can stand on its own and each can be combined with others, but where, if all are taken together, the best result is achieved (the "super product").
Intended use is web. See attached file as an example.
The most basic idea is as the attached diagram shows, where 4 rectangles are arranged in a quadrangle, with a middle rectangle in the center representing the combined 4 products. This concept is fine except it is a bit too obvious as it stands. We are looking for either a variation of this or another concept.
The audience is technical + professional + enterprise - NOT consumers. Hence the design should be conservative in nature.
We are aware of tools like as Canva or Pictogram where such graphics are available, but we are looking for something with a bit more imagination and flexibility.
This graphic should be targeted to web sites and be delivered with vector-based (SVG) graphics.

```html
<!DOCTYPE html>
<html lang="en">
<head>
<meta charset="utf-8">
<title>Four in One – Super Product</title>
<link rel="stylesheet" href="https://fonts.googleapis.com/css2?family=Oswald:wght@600;700&family=Poppins:wght@400;600;700&display=swap">
<style>
  :root {
    --bg: #4b4b4b;
    --card: #ffffff;
    --ink: #111111;
    --navy: #0d0d3f;
    --red: #d90000;
    --red-light: #f2643c;
    --amber: #f5b400;
    --orange: #ef8a2e;
    --purple: #8b3fe0;
    --purple-light: #b266f5;
    --blue: #1f78e8;
    --blue-light: #3c9cf0;
  }
  * { box-sizing: border-box; margin: 0; padding: 0; }
  html, body { width: 1200px; height: 1091px; overflow: hidden; background: var(--bg); }
  body { position: relative; font-family: "Poppins", sans-serif; color: var(--ink); }

  .card {
    position: absolute; width: 491px; height: 369px; background: var(--card);
    border-top: 9px solid; box-shadow: 0 10px 24px rgba(0,0,0,.35);
  }
  .card--docs { left: 71px; top: 138px; border-color: var(--red); border-right: 3px solid var(--red); border-radius: 0 100px 0 100px; }
  .card--security { left: 638px; top: 138px; border-color: var(--orange); border-left: 3px solid var(--orange); border-radius: 100px 0 100px 0; }
  .card--erp { left: 71px; top: 584px; border-color: var(--purple); border-left: 3px solid var(--purple); border-radius: 100px 0 100px 0; }
  .card--digital { left: 638px; top: 584px; border-color: var(--blue); border-right: 3px solid var(--blue); border-radius: 0 100px 0 100px; }

  .icon-tab {
    position: absolute; top: -9px; width: 90px; height: 86px; border-radius: 0 0 6px 6px;
    display: flex; align-items: center; justify-content: center;
  }
  .card--docs .icon-tab { left: 67px; background: linear-gradient(180deg, var(--red-light), #e8442a); }
  .card--security .icon-tab { right: 69px; background: linear-gradient(180deg, #f5a43a, var(--orange)); }
  .card--erp .icon-tab { left: 67px; background: linear-gradient(180deg, var(--purple-light), var(--purple)); }
  .card--digital .icon-tab { right: 69px; background: linear-gradient(180deg, var(--blue), var(--blue-light)); }

  .title {
    position: absolute; font-family: "Oswald", sans-serif; font-weight: 600;
    font-size: 29px; line-height: 35px; letter-spacing: -.2px;
  }
  .card--docs .title { left: 175px; top: 17px; color: var(--red); }
  .card--security .title { right: 182px; top: 18px; text-align: right; color: var(--amber); }
  .card--erp .title { left: 171px; top: 22px; color: var(--purple); }
  .card--digital .title { right: 177px; top: 27px; text-align: right; color: var(--blue); }

  .summary { position: absolute; font-size: 14.4px; line-height: 17.6px; width: 380px; }
  .card--docs .summary { left: 65px; top: 115px; }
  .card--security .summary { right: 66px; top: 117px; text-align: right; }
  .card--erp .summary { left: 65px; top: 115px; }
  .card--digital .summary { right: 64px; top: 108px; text-align: right; }

  .features { position: absolute; list-style: none; font-weight: 600; font-size: 15.8px; }
  .features li { display: flex; align-items: center; gap: 8px; height: 27.5px; }
  .card--docs .features { left: 66px; top: 187px; }
  .card--security .features { right: 66px; top: 188px; }
  .card--security .features li, .card--digital .features li { justify-content: flex-end; height: 25.2px; }
  .card--erp .features { left: 66px; top: 195px; }
  .card--erp .features li { height: 25.6px; }
  .card--digital .features { right: 66px; top: 195px; }
  .card--digital .features li { height: 25.6px; }
  .tick { width: 11px; height: 11px; flex: none; }

  .btn {
    position: absolute; height: 30px; border-radius: 15px; color: #fff; font-weight: 600;
    font-size: 14px; display: flex; align-items: center; padding: 0 13px;
    box-shadow: 0 2px 4px rgba(0,0,0,.2);
  }
  .card--docs .btn { left: 66px; top: 305px; background: linear-gradient(180deg, #ee1a1a, #c80000); }
  .card--security .btn { right: 68px; top: 306px; background: linear-gradient(180deg, #f7b04b, var(--orange)); }
  .card--erp .btn { left: 66px; top: 305px; background: linear-gradient(180deg, var(--purple-light), var(--purple)); }
  .card--digital .btn { right: 68px; top: 305px; background: linear-gradient(180deg, var(--blue-light), var(--blue)); }

  .hub {
    position: absolute; left: 464px; top: 416px; width: 272px; height: 272px; border-radius: 50%;
    background: conic-gradient(#ffc800 0 90deg, #0a6ff0 90deg 180deg, #a653f2 180deg 270deg, #e80000 270deg 360deg);
    box-shadow: 0 10px 22px rgba(0,0,0,.35);
  }
  .hub__core {
    position: absolute; left: 45px; top: 45px; width: 182px; height: 182px; border-radius: 50%;
    background: radial-gradient(circle at 50% 35%, #ffffff, #eeeeee);
    box-shadow: 0 4px 10px rgba(0,0,0,.3);
    display: flex; align-items: center; justify-content: center; text-align: center;
    font-family: "Oswald", sans-serif; font-weight: 700; font-size: 35px; line-height: 36px; color: var(--navy);
  }
</style>
</head>
<body>

<section class="card card--docs">
  <div class="icon-tab">
    <svg width="44" height="44" viewBox="0 0 44 44" fill="none" stroke="#fff" stroke-width="3" stroke-linejoin="round">
      <path d="M8 3h18l9 9v12M8 3v36h16M26 3v9h9"/>
      <path d="M13 18h14M13 24h10M13 30h8"/>
      <circle cx="33" cy="34" r="5" fill="#fff"/>
      <path d="M33 26v3M33 39v3M25 34h3M38 34h3M27.5 28.5l2 2M36.5 37.5l2 2M27.5 39.5l2-2M36.5 30.5l2-2"/>
    </svg>
  </div>
  <h2 class="title">Document<br>Management</h2>
  <p class="summary">Streamline document organization, access, and collaboration with easier file storage and sharing, leading to more efficient workflows.</p>
  <ul class="features">
    <li><svg class="tick" viewBox="0 0 12 12"><circle cx="6" cy="6" r="6" fill="#d90000"/><path d="M3.3 6.2l1.8 1.8 3.6-3.7" stroke="#fff" stroke-width="1.6" fill="none"/></svg>Centralized Document Control</li>
    <li><svg class="tick" viewBox="0 0 12 12"><circle cx="6" cy="6" r="6" fill="#d90000"/><path d="M3.3 6.2l1.8 1.8 3.6-3.7" stroke="#fff" stroke-width="1.6" fill="none"/></svg>Collaborative Workspace Integration</li>
    <li><svg class="tick" viewBox="0 0 12 12"><circle cx="6" cy="6" r="6" fill="#d90000"/><path d="M3.3 6.2l1.8 1.8 3.6-3.7" stroke="#fff" stroke-width="1.6" fill="none"/></svg>Automated Compliance Tracking</li>
    <li><svg class="tick" viewBox="0 0 12 12"><circle cx="6" cy="6" r="6" fill="#d90000"/><path d="M3.3 6.2l1.8 1.8 3.6-3.7" stroke="#fff" stroke-width="1.6" fill="none"/></svg>Check 4</li>
  </ul>
  <span class="btn">Learn More</span>
</section>

<section class="card card--security">
  <div class="icon-tab">
    <svg width="50" height="50" viewBox="0 0 50 50" fill="none" stroke="#fff" stroke-width="2.6">
      <path d="M8 30A19 19 0 0 0 42 30M42 20A19 19 0 0 0 8 20"/>
      <path d="M25 9l11 4v10c0 8-5 13-11 16c-6-3-11-8-11-16V13z" fill="#fff" stroke="none"/>
      <rect x="20.5" y="21" width="9" height="8" rx="1" fill="#ef8a2e" stroke="none"/>
      <path d="M22.5 21v-3a2.5 2.5 0 0 1 5 0v3" stroke="#ef8a2e" stroke-width="2"/>
    </svg>
  </div>
  <h2 class="title">Security and<br>Compliance</h2>
  <p class="summary">Benefit from tailored cloud solutions, secure data storage, and expert disaster recovery planning for reliable and scalable IT operations.</p>
  <ul class="features">
    <li>Custom Cloud Solutions<svg class="tick" viewBox="0 0 12 12"><circle cx="6" cy="6" r="6" fill="#f0a020"/><path d="M3.3 6.2l1.8 1.8 3.6-3.7" stroke="#fff" stroke-width="1.6" fill="none"/></svg></li>
    <li>Secure Data Storage<svg class="tick" viewBox="0 0 12 12"><circle cx="6" cy="6" r="6" fill="#f0a020"/><path d="M3.3 6.2l1.8 1.8 3.6-3.7" stroke="#fff" stroke-width="1.6" fill="none"/></svg></li>
    <li>Expert Disaster Recovery<svg class="tick" viewBox="0 0 12 12"><circle cx="6" cy="6" r="6" fill="#f0a020"/><path d="M3.3 6.2l1.8 1.8 3.6-3.7" stroke="#fff" stroke-width="1.6" fill="none"/></svg></li>
    <li>Check 4<svg class="tick" viewBox="0 0 12 12"><circle cx="6" cy="6" r="6" fill="#f0a020"/><path d="M3.3 6.2l1.8 1.8 3.6-3.7" stroke="#fff" stroke-width="1.6" fill="none"/></svg></li>
  </ul>
  <span class="btn">Learn More</span>
</section>

<section class="card card--erp">
  <div class="icon-tab">
    <svg width="52" height="52" viewBox="0 0 52 52" fill="none" stroke="#fff" stroke-width="2.4">
      <rect x="14" y="14" width="24" height="24" rx="2"/>
      <circle cx="26" cy="26" r="6"/>
      <path d="M20 14V8M26 14V6M32 14V8M20 38v6M26 38v8M32 38v6M14 20H8M14 26H6M14 32H8M38 20h6M38 26h8M38 32h6"/>
      <g fill="#fff" stroke="none"><circle cx="20" cy="7" r="2.2"/><circle cx="32" cy="7" r="2.2"/><circle cx="20" cy="45" r="2.2"/><circle cx="32" cy="45" r="2.2"/><circle cx="7" cy="20" r="2.2"/><circle cx="7" cy="32" r="2.2"/><circle cx="45" cy="20" r="2.2"/><circle cx="45" cy="32" r="2.2"/></g>
    </svg>
  </div>
  <h2 class="title">Enterprise<br>Resource Planning</h2>
  <p class="summary">Simplify management across finance, sales, and operations, enabling better decision-making and improved productivity.</p>
  <ul class="features">
    <li><svg class="tick" viewBox="0 0 12 12"><circle cx="6" cy="6" r="6" fill="#a35cf0"/><path d="M3.3 6.2l1.8 1.8 3.6-3.7" stroke="#fff" stroke-width="1.6" fill="none"/></svg>Integrated Business Processes</li>
    <li><svg class="tick" viewBox="0 0 12 12"><circle cx="6" cy="6" r="6" fill="#a35cf0"/><path d="M3.3 6.2l1.8 1.8 3.6-3.7" stroke="#fff" stroke-width="1.6" fill="none"/></svg>Enhanced Decision-Making</li>
    <li><svg class="tick" viewBox="0 0 12 12"><circle cx="6" cy="6" r="6" fill="#a35cf0"/><path d="M3.3 6.2l1.8 1.8 3.6-3.7" stroke="#fff" stroke-width="1.6" fill="none"/></svg>Productivity Improvement</li>
    <li><svg class="tick" viewBox="0 0 12 12"><circle cx="6" cy="6" r="6" fill="#a35cf0"/><path d="M3.3 6.2l1.8 1.8 3.6-3.7" stroke="#fff" stroke-width="1.6" fill="none"/></svg>Check 4</li>
  </ul>
  <span class="btn">Learn More</span>
</section>

<section class="card card--digital">
  <div class="icon-tab">
    <svg width="52" height="52" viewBox="0 0 52 52" fill="none" stroke="#fff" stroke-width="3">
      <path d="M26 8v5M26 39v5M8 26h5M13.3 13.3l3.5 3.5M13.3 38.7l3.5-3.5" stroke-width="5"/>
      <path d="M30 14a12 12 0 1 0 0 24"/>
      <path d="M30 18h6l4-5M30 26h12M30 34h6l4 5"/>
      <g fill="#fff" stroke="none"><circle cx="42" cy="12" r="3"/><circle cx="45" cy="26" r="3"/><circle cx="42" cy="40" r="3"/></g>
    </svg>
  </div>
  <h2 class="title">Digital<br>Transformation</h2>
  <p class="summary">Turn scanned documents into easily searchable digital archives, boosting efficiency and accessibility.</p>
  <ul class="features">
    <li>Instant searchable Archives with OCR<svg class="tick" viewBox="0 0 12 12"><circle cx="6" cy="6" r="6" fill="#1f78e8"/><path d="M3.3 6.2l1.8 1.8 3.6-3.7" stroke="#fff" stroke-width="1.6" fill="none"/></svg></li>
    <li>Automated Document Classification<svg class="tick" viewBox="0 0 12 12"><circle cx="6" cy="6" r="6" fill="#1f78e8"/><path d="M3.3 6.2l1.8 1.8 3.6-3.7" stroke="#fff" stroke-width="1.6" fill="none"/></svg></li>
    <li>DocuPortal and Cloud Blob Ready<svg class="tick" viewBox="0 0 12 12"><circle cx="6" cy="6" r="6" fill="#1f78e8"/><path d="M3.3 6.2l1.8 1.8 3.6-3.7" stroke="#fff" stroke-width="1.6" fill="none"/></svg></li>
    <li>Check 4<svg class="tick" viewBox="0 0 12 12"><circle cx="6" cy="6" r="6" fill="#1f78e8"/><path d="M3.3 6.2l1.8 1.8 3.6-3.7" stroke="#fff" stroke-width="1.6" fill="none"/></svg></li>
  </ul>
  <span class="btn">Learn More</span>
</section>

<div class="hub">
  <div class="hub__core">SUPER<br>PRODUCT</div>
</div>

</body>
</html>
```